Wealth Management Business Card

We are a professional services consulting firm that specializes in high net worth individuals over $25,000,000, executives C-suite and above, closely held businesses owners, family offices and highly compensated employees.

Our focus is on risk mitigation and tax efficient strategies. Our clients take their risk on themselves and have a proven track record generating wealth. Our directive is to preserve and protect the wealth they’ve already created.

Our company Harbridge Advisory is geared around five directives of asset protection:
1) Legal Structuring
2) Leverage & Financing
3) Risk Management - Asset Protection & Insurance, Trustee Work
4) Asset Management & Investing - Under www.qelvantcapital.com
5) Tax Efficient Strategies

Our Company Mark is a Pentagon with a key in the middle. A pentagon is the most efficient defensive structure. Each point of a pentagon is equal distance front every point . Each side provides support to another and works together, which is the key to our clients success.

Our key colors are blue, black and silver.

We ‘re located in the Pacific Northwest with bi coastal and international clients. We have fewer, higher net worth clients and provide exceptional customer service. We do not do social media.

website is www.harbridgepath.com

Target Market(s)

High End Clients

Contact Information for Business Card

extra thick

Font styles to use
Serif

Requirements
Must have
• Metalic foil for lettering.
Black Background on one side
White Background on the other
Horizontal Format Only
No Rounded corners
Not Marketing sales information on the card.
Nice to have
• imprinted texture on the card
Should not have
• lots of color

```html
<!DOCTYPE html>
<html lang="en">
<head>
<meta charset="utf-8">
<title>Harbridge Advisory – Business Card</title>
<link href="https://fonts.googleapis.com/css2?family=Exo+2:wght@400;500;600&family=Cinzel:wght@700&display=swap" rel="stylesheet">
<style>
  :root {
    --stage: #1c1c1e;
    --card-white: #ffffff;
    --card-black: #0c0c0e;
    --navy: #15296e;
    --ink: #2e2e30;
    --muted: #55585e;
    --accent: #1a6fc0;
    --silver: #c4c8ce;
    --silver-dim: #8a8f96;
    --on-accent: #ffffff;
  }
  * { box-sizing: border-box; margin: 0; padding: 0; }
  html, body {
    width: 1200px; height: 1200px; overflow: hidden;
    background: var(--stage);
    font-family: "Exo 2", "Segoe UI", sans-serif;
  }
  .canvas { position: relative; width: 1200px; height: 1200px; }
  .card {
    position: absolute; left: 180px;
    width: 840px; height: 480px;
    overflow: hidden;
  }

  /* Front – white */
  .card-front {
    top: 90px; background: var(--card-white);
    display: flex; align-items: center;
  }
  .front-brand {
    width: 360px; text-align: center;
    font-family: "Cinzel", Georgia, serif; font-weight: 700;
    font-size: 38px; line-height: 1.2; color: var(--navy);
  }
  .brand-mark {
    display: block; width: 24px; height: 24px; margin: 0 auto 22px;
    background: var(--navy);
  }
  .front-divider { width: 2px; height: 300px; background: var(--silver); }
  .front-details { flex: 1; padding: 0 50px 0 48px; }
  .holder-name {
    font-size: 50px; font-weight: 400; color: var(--ink); line-height: 1; white-space: nowrap;
  }
  .holder-title {
    display: inline-block; margin-top: 12px; padding: 3px 10px;
    background: var(--accent); color: var(--on-accent);
    font-size: 22px; font-weight: 500;
  }
  .contact-heading {
    margin-top: 28px; font-size: 25px; font-weight: 500; color: var(--accent);
  }
  .contact-list { margin-top: 10px; list-style: none; font-size: 17px; color: var(--muted); line-height: 1.4; }
  .contact-rule { margin-top: 12px; height: 3px; background: var(--accent); }
  .contact-web { margin-top: 8px; font-size: 17px; color: var(--accent); }

  /* Back – black */
  .card-back {
    top: 620px; background: var(--card-black);
    display: flex; flex-direction: column; align-items: center; justify-content: center;
    text-align: center;
  }
  .back-mark { width: 30px; height: 30px; background: var(--silver); margin-bottom: 30px; }
  .back-brand {
    font-family: "Cinzel", Georgia, serif; font-weight: 700;
    font-size: 58px; line-height: 1.15; color: var(--silver);
  }
  .back-rule { width: 260px; height: 2px; background: var(--silver-dim); margin-top: 30px; }
</style>
</head>
<body>
<main class="canvas">
  <section class="card card-front" aria-label="Card front">
    <div class="front-brand"><span class="brand-mark"></span>Harbridge<br>Advisory</div>
    <div class="front-divider"></div>
    <div class="front-details">
      <h1 class="holder-name">Reid Calloway</h1>
      <p class="holder-title">Managing Director</p>
      <h2 class="contact-heading">Contact Details</h2>
      <ul class="contact-list">
        <li>Email: reid@lumenfairway.net</li>
        <li>Email: info@qelvantcapital.com</li>
        <li>Mobile: (555) 014-2290</li>
      </ul>
      <div class="contact-rule"></div>
      <p class="contact-web">www.qelvantcapital.com</p>
    </div>
  </section>

  <section class="card card-back" aria-label="Card back">
    <span class="back-mark"></span>
    <div class="back-brand">Harbridge<br>Advisory</div>
    <div class="back-rule"></div>
  </section>
</main>
</body>
</html>
```